New Wix logo and website layout

I need a new logo design and a new, modern website layout design. I am a professional therapist providing remedial massage. I am Canadian but live in Australia & would like the logo to have a somewhat 'Canadian feel' to it (something subtle i.e. no flags) I currently have a maple tree leaf as my logo. my current website is tidewellbodyworks.com.au. I need the website to work on mobile phones & traditional web browsers.

Target Market(s)

customers looking for remedial massage and manual lymphatic drainage

Industry/Entity Type

professional massage

Coding

Coded - Design and coding required

Font styles to use
Sans Serif

Colors
EB3D1F
EC4F4E
F09395
F8D3D4
FCEDEE

Requirements
Nice to have
• something subtle that indicates that I am canadian
Should not have
• no flags. nothing too bold

```html
<!DOCTYPE html>
<html lang="en">
<head>
<meta charset="utf-8">
<title>Tidewell Bodyworks</title>
<link href="https://fonts.googleapis.com/css2?family=Poppins:wght@400;500;600;700&family=Arimo:wght@400;700&display=swap" rel="stylesheet">
<style>
:root{
  --red:#eb3d1f;
  --red-soft:#ec4f4e;
  --pink:#f09395;
  --blush:#f8d3d4;
  --mist:#fcedee;
  --ink:#222222;
  --text:#444444;
  --grey-bg:#f5f5f5;
  --black:#0b0b0b;
  --white:#ffffff;
}
*{box-sizing:border-box;margin:0;padding:0}
html,body{width:1200px;height:4185px;overflow:hidden;background:var(--white)}
body{font-family:"Arimo",Arial,sans-serif;color:var(--text)}
.page{position:relative;width:1200px;height:4185px;overflow:hidden}
.abs{position:absolute}
h2.section-title{position:absolute;left:0;width:1200px;text-align:center;font-family:"Poppins",sans-serif;font-weight:500;font-size:37px;color:var(--ink)}
.title-rule{position:absolute;width:48px;height:3px;background:var(--red)}
.lead{position:absolute;left:0;width:1200px;text-align:center;font-size:13.5px;line-height:23px;color:var(--text)}

/* hero */
.hero-photo{position:absolute;left:0;top:0;width:1200px;height:870px;
  background:radial-gradient(ellipse at 75% 40%,#f6c25a 0%,#f0a030 30%,#d9751a 60%,#8a4a14 100%)}
.hero-wave{position:absolute;left:0;top:640px}
.brand-box{position:absolute;left:112px;top:0;width:143px;height:179px;background:var(--white);border-radius:0 0 72px 72px;display:flex;flex-direction:column;align-items:center;justify-content:center;padding-top:20px}
.brand-box .dot{width:64px;height:64px;border-radius:50%;border:3px solid var(--red);margin-bottom:10px}
.brand-box .name{font-family:"Poppins",sans-serif;font-weight:600;font-size:15px;line-height:18px;color:var(--ink);text-align:center;letter-spacing:.5px}
.topbar{position:absolute;top:23px;left:305px;font-family:"Poppins",sans-serif;font-size:13px;color:var(--white);display:flex;gap:28px;align-items:center}
.topbar span{display:flex;align-items:center;gap:10px}
.nav{position:absolute;left:244px;top:68px;width:771px;height:67px;background:var(--white);border-radius:0 34px 34px 0}
.nav a{position:absolute;top:24px;font-family:"Poppins",sans-serif;font-size:15px;color:var(--ink);text-decoration:none}
.nav a.active{color:var(--red)}
.hero-title{position:absolute;left:590px;top:430px;font-family:"Poppins",sans-serif;font-weight:600;font-size:47px;color:var(--white);letter-spacing:.5px}
.hero-sub{position:absolute;left:592px;top:502px;font-family:"Poppins",sans-serif;font-weight:500;font-size:19px;line-height:35px;color:var(--white)}
.btn{position:absolute;display:flex;align-items:center;justify-content:center;background:var(--red);color:var(--white);font-family:"Poppins",sans-serif;font-weight:500;border-radius:30px}
.dots{position:absolute;left:918px;top:809px;display:flex;gap:8px}
.dots i{width:10px;height:10px;border-radius:50%;background:var(--white)}
.dots i.on{background:var(--red)}

/* services */
.service{position:absolute;width:274px;height:274px;border-radius:50%;overflow:hidden}
.service svg{position:absolute;left:0;bottom:0}
.service .label{position:absolute;left:0;bottom:22px;width:100%;text-align:center;font-family:"Poppins",sans-serif;font-weight:600;font-size:21px;color:var(--white)}

/* about */
.about-text{position:absolute;left:651px;top:1898px;width:440px;font-size:13.5px;line-height:25.8px;color:var(--text);text-align:justify}
.about-text p+p{margin-top:16px}
.about-title{position:absolute;left:651px;top:1812px;font-family:"Poppins",sans-serif;font-weight:500;font-size:40px;color:var(--ink)}

/* fees */
.fee-row{position:absolute;left:330px;width:539px;height:60px;border-bottom:1.5px solid var(--pink)}
.fee-row .service-name{position:absolute;left:16px;top:25px;font-family:"Poppins",sans-serif;font-size:17px;color:var(--text)}
.fee-row .price{position:absolute;right:0;top:6px;width:58px;height:58px;border-radius:50%;border:2px solid var(--red);background:var(--white);display:flex;align-items:center;justify-content:center;font-family:"Poppins",sans-serif;font-weight:600;font-size:16px;color:var(--red)}

/* contact */
.contact-bg{position:absolute;left:0;top:2980px;width:1200px;height:700px;background:var(--grey-bg)}
.map{position:absolute;left:110px;top:3186px;width:418px;height:338px;border:4px solid var(--white);box-shadow:0 0 3px rgba(0,0,0,.2);background:linear-gradient(135deg,#e9ebe7 0%,#dfe6dc 55%,#a7d7a1 100%)}
.field-label{position:absolute;font-size:12px;color:var(--ink);letter-spacing:.3px}
.field{position:absolute;background:var(--white);border:1px solid #c9c9c9}

/* footer */
.footer-wave{position:absolute;left:0;top:3560px}
.footer-brand{position:absolute;left:140px;top:3786px;width:234px;text-align:center}
.footer-brand .dot{width:104px;height:104px;border-radius:50%;border:3px solid var(--red);margin:0 auto 16px}
.footer-brand .name{font-family:"Poppins",sans-serif;font-weight:600;font-size:24px;line-height:28px;color:var(--white)}
.badge{position:absolute;left:130px;top:3963px;width:237px;height:80px;border-radius:8px;background:#2a2a2a}
.footer-heading{position:absolute;font-family:"Poppins",sans-serif;font-weight:600;font-size:20px;color:var(--white)}
.contact-item{position:absolute;left:451px;display:flex;gap:20px;color:var(--white)}
.contact-item svg{flex:none;margin-top:4px}
.contact-item b{display:block;font-family:"Poppins",sans-serif;font-weight:600;font-size:17px;line-height:22px}
.contact-item span{font-size:15px;line-height:22px}
.hours{position:absolute;left:767px;top:3842px;width:300px;color:var(--white);font-size:14.5px}
.hours .row{display:flex;align-items:center;height:30px}
.hours .day{width:86px}
.hours .lead-line{flex:1;border-bottom:1px dashed #888;margin:0 12px 0 0;height:1px;align-self:center;max-width:110px;margin-left:0}
.hours .time{margin-left:8px}
.footer-rule{position:absolute;left:110px;top:4104px;width:980px;height:1px;background:#333}
.copyright{position:absolute;left:0;top:4133px;width:1200px;text-align:center;color:var(--white);font-size:15px}
</style>
</head>
<body>
<div class="page">

  <!-- Hero -->
  <div class="hero-photo" role="img" aria-label="Autumn maple foliage in warm orange and gold tones"></div>
  <svg class="hero-wave" width="1200" height="240" viewBox="0 640 1200 240" aria-hidden="true">
    <path d="M0 805 C150 720 300 690 450 715 C650 750 800 850 1000 843 C1100 838 1160 815 1200 790 L1200 880 L0 880Z" fill="#ffffff"/>
    <path d="M30 800 C200 690 400 700 600 790 C760 855 880 880 985 868 C860 852 730 828 600 797 C420 735 230 705 30 800Z" fill="#eb3d1f"/>
  </svg>

  <div class="brand-box">
    <div class="dot"></div>
    <div class="name">TIDEWELL<br>BODYWORKS</div>
  </div>

  <div class="topbar">
    <span><svg width="10" height="14" viewBox="0 0 10 14"><path d="M5 0C2.2 0 0 2.2 0 5c0 3.6 5 9 5 9s5-5.4 5-9c0-2.8-2.2-5-5-5zm0 7a2 2 0 110-4 2 2 0 010 4z" fill="#fff"/></svg>Clara Voss 24 Larkspur Avenue Fernbrook VIC 3199</span>
    <span><svg width="13" height="10" viewBox="0 0 13 10"><rect width="13" height="10" rx="1" fill="#fff"/><path d="M0 1l6.5 5L13 1" stroke="#e89a3a" fill="none"/></svg>clara@tidewellbodyworks.com.au</span>
  </div>

  <nav class="nav">
    <a class="active" style="left:252px">Home</a>
    <a style="left:347px">Services</a>
    <a style="left:461px">About Me</a>
    <a style="left:583px">Fees</a>
    <a style="left:668px">Contact</a>
  </nav>

  <h1 class="hero-title">TIDEWELL BODYWORKS</h1>
  <p class="hero-sub">SED UT PERSPICIATIS UNDE OMNIS ISTE NATUS ERROR<br>SIT VOLUPTATEM ACCUSANTIUM DOLOREM</p>
  <div class="btn" style="left:591px;top:591px;width:164px;height:54px;font-size:16px">GET STARTED</div>
  <div class="dots"><i></i><i class="on"></i><i></i></div>

  <!-- Remedial Massage -->
  <h2 class="section-title" style="top:905px">Remedial Massage</h2>
  <div class="title-rule" style="left:576px;top:960px"></div>
  <p class="lead" style="top:980px">Sed ut perspiciatis unde omnis iste natus error sit voluptatem accusantium doloremque laudantium</p>

  <div class="service" style="left:136px;top:1045px;background:linear-gradient(160deg,#d9c7bd,#8f6a55 60%,#3c2b24)" role="img" aria-label="Therapist massaging a client's shoulders">
    <svg width="274" height="110" viewBox="0 0 274 110"><path d="M0 70 C90 40 190 10 274 0 L274 110 L0 110Z" fill="#eb3d1f"/></svg>
    <div class="label">Remedial</div>
  </div>
  <div class="service" style="left:462px;top:1045px;background:linear-gradient(160deg,#f2ede6,#d8c2a8 55%,#a37d5c)" role="img" aria-label="Therapist giving a deep tissue back massage">
    <svg width="274" height="110" viewBox="0 0 274 110"><path d="M0 70 C90 40 190 10 274 0 L274 110 L0 110Z" fill="#eb3d1f"/></svg>
    <div class="label">Deep Tissue</div>
  </div>
  <div class="service" style="left:792px;top:1045px;background:linear-gradient(160deg,#f4f4f6,#d8d2cf 55%,#b49d90)" role="img" aria-label="Relaxation massage on a client's leg">
    <svg width="274" height="110" viewBox="0 0 274 110"><path d="M0 70 C90 40 190 10 274 0 L274 110 L0 110Z" fill="#eb3d1f"/></svg>
    <div class="label">Relaxation</div>
  </div>
  <div class="service" style="left:292px;top:1331px;background:radial-gradient(circle at 40% 40%,#f7b27a,#f2d6c6 55%,#e8dcd6)" role="img" aria-label="Pregnancy massage, hands on a pregnant belly">
    <svg width="274" height="110" viewBox="0 0 274 110"><path d="M0 70 C90 40 190 10 274 0 L274 110 L0 110Z" fill="#eb3d1f"/></svg>
    <div class="label">Pregnancy</div>
  </div>
  <div class="service" style="left:621px;top:1331px;background:linear-gradient(160deg,#b58463,#7b4a32 55%,#1e1614)" role="img" aria-label="Lymphatic drainage massage on a client's leg">
    <svg width="274" height="110" viewBox="0 0 274 110"><path d="M0 70 C90 40 190 10 274 0 L274 110 L0 110Z" fill="#eb3d1f"/></svg>
    <div class="label">Lymphatic</div>
  </div>

  <!-- About -->
  <svg class="abs" style="left:0;top:1670px" width="1200" height="690" viewBox="0 0 1200 690" role="img" aria-label="Soft blurred seaside backdrop in pale blue">
    <defs>
      <linearGradient id="aboutSky" x1="0" y1="0" x2="0" y2="1">
        <stop offset="0" stop-color="#eaf8fe"/>
        <stop offset=".55" stop-color="#bcd8ea"/>
        <stop offset=".8" stop-color="#98b8c6"/>
        <stop offset="1" stop-color="#c9d8cf"/>
      </linearGradient>
    </defs>
    <path d="M0 130 C300 20 700 0 1200 120 L1200 540 C1000 620 800 670 600 670 C350 670 150 610 0 550Z" fill="url(#aboutSky)"/>
    <path d="M200 60 C500 -10 900 20 1200 115 L1200 130 C900 45 520 10 200 60Z" fill="#eb3d1f"/>
    <path d="M0 555 C200 625 400 670 620 672 C850 672 1050 610 1200 545 L1200 555 C1050 625 850 686 620 686 C400 686 200 640 0 570Z" fill="#eb3d1f"/>
  </svg>
  <svg class="abs" style="left:129px;top:1792px" width="446" height="446" viewBox="0 0 446 446" aria-hidden="true">
    <circle cx="223" cy="223" r="223" fill="#eb3d1f"/>
  </svg>
  <div class="abs" style="left:149px;top:1797px;width:410px;height:410px;border-radius:50%;background:linear-gradient(160deg,#f3f1ee,#d9d5cf 50%,#9fb2cf)" role="img" aria-label="Portrait of the therapist in a bright office"></div>

  <h2 class="about-title">About Me</h2>
  <div class="title-rule" style="left:651px;top:1870px"></div>
  <div class="about-text">
    <p>I completed my training in Toronto, Canada in 1999 where I obtained a Diploma of Remedial Massage through the Northern College of Massage &amp; Hydrotherapy.</p>
    <p>Over the years, I have practiced in several different settings including medical centre, chiropractic clinic, spa and currently am a sole trader in my own practice. I have been helping my clients achieve better health through my treatments for several years. I take special interest in women's health.</p>
  </div>
  <div class="btn" style="left:650px;top:2153px;width:160px;height:56px;font-size:17px">Read More</div>

  <!-- Fees -->
  <h2 class="section-title" style="top:2388px">Fee Schedule</h2>
  <div class="title-rule" style="left:576px;top:2442px"></div>
  <p class="lead" style="top:2466px">I am registered with most health funds. Check your level of cover to see if you are<br>able to claim for remedial massage.</p>

  <div class="fee-row" style="top:2550px"><span class="service-name">30 min Remedial Massage</span><span class="price">$70</span></div>
  <div class="fee-row" style="top:2624px"><span class="service-name">45&nbsp; min Remedial Massage</span><span class="price">$90</span></div>
  <div class="fee-row" style="top:2698px"><span class="service-name">60 min&nbsp; Remedial Massage</span><span class="price">$110</span></div>
  <div class="fee-row" style="top:2771px"><span class="service-name">90 min Remedial Massage</span><span class="price">$160</span></div>
  <div class="fee-row" style="top:2845px"><span class="service-name">Manual Lymphatic Drainage</span><span class="price">$140</span></div>

  <!-- Contact -->
  <div class="contact-bg"></div>
  <h2 class="section-title" style="top:3015px">Contact Us</h2>
  <div class="title-rule" style="left:576px;top:3070px"></div>
  <p class="lead" style="top:3094px">I am registered with most health funds. Check your level of cover to see if you are<br>able to claim for remedial massage.</p>

  <div class="map" role="img" aria-label="Street map showing the clinic location"></div>

  <span class="field-label" style="left:560px;top:3189px">FIRST NAME</span>
  <div class="field" style="left:560px;top:3207px;width:255px;height:37px"></div>
  <span class="field-label" style="left:833px;top:3189px">LAST NAME</span>
  <div class="field" style="left:833px;top:3207px;width:255px;height:37px"></div>
  <span class="field-label" style="left:560px;top:3268px">EMAIL</span>
  <div class="field" style="left:560px;top:3287px;width:255px;height:37px"></div>
  <span class="field-label" style="left:833px;top:3268px">PHONE</span>
  <div class="field" style="left:833px;top:3287px;width:255px;height:37px"></div>
  <span class="field-label" style="left:560px;top:3346px">MESSAGE</span>
  <div class="field" style="left:560px;top:3363px;width:528px;height:100px"></div>
  <div class="btn" style="left:560px;top:3485px;width:132px;height:47px;font-size:16px">SUBMIT</div>

  <!-- Footer -->
  <svg class="footer-wave" width="1200" height="625" viewBox="0 3560 1200 625" aria-hidden="true">
    <path d="M0 3675 C200 3600 400 3600 650 3695 C850 3770 1050 3740 1200 3650 L1200 4185 L0 4185Z" fill="#0b0b0b"/>
    <path d="M205 3590 C400 3560 520 3620 680 3690 C860 3760 1030 3720 1160 3655 C1040 3740 860 3775 670 3705 C520 3650 380 3590 205 3590Z" fill="#eb3d1f"/>
  </svg>

  <div class="footer-brand">
    <div class="dot"></div>
    <div class="name">TIDEWELL<br>BODYWORKS</div>
  </div>
  <div class="badge" aria-label="Partner association badge"></div>

  <h3 class="footer-heading" style="left:451px;top:3794px">CONTACT US</h3>
  <div class="contact-item" style="top:3846px">
    <svg width="20" height="24" viewBox="0 0 20 24"><path d="M10 1C5 1 1.5 4.8 1.5 9.5 1.5 16 10 23 10 23s8.5-7 8.5-13.5C18.5 4.8 15 1 10 1z" fill="none" stroke="#fff" stroke-width="1.4"/><circle cx="10" cy="9.5" r="3" fill="none" stroke="#fff" stroke-width="1.4"/></svg>
    <div><b>ADDRESS</b><span>24 Larkspur Avenue<br>Fernbrook VIC 3199</span></div>
  </div>
  <div class="contact-item" style="top:3931px">
    <svg width="20" height="20" viewBox="0 0 20 20"><path d="M4 1l4 4-2 3c1 2.5 3.5 5 6 6l3-2 4 4-3 3C8 18 2 12 1 4z" fill="none" stroke="#fff" stroke-width="1.4"/></svg>
    <div><b>PHONE</b><span>0400 555 218</span></div>
  </div>
  <div class="contact-item" style="top:4001px">
    <svg width="20" height="16" viewBox="0 0 20 16"><rect x="1" y="1" width="18" height="14" fill="none" stroke="#fff" stroke-width="1.4"/><path d="M1 1l9 7 9-7" fill="none" stroke="#fff" stroke-width="1.4"/></svg>
    <div><b>EMAIL</b><span>clara@tidewellbodyworks.com.au</span></div>
  </div>

  <h3 class="footer-heading" style="left:767px;top:3791px">OPENING HOURS</h3>
  <div class="hours">
    <div class="row"><span class="day">Monday</span><span class="lead-line"></span><span class="time">9:00 - 10:00</span></div>
    <div class="row"><span class="day">Tuesday</span><span class="lead-line"></span><span class="time">9:00 - 10:00</span></div>
    <div class="row"><span class="day">Wednesday</span><span class="lead-line"></span><span class="time">9:00 - 10:00</span></div>
    <div class="row"><span class="day">Thursday</span><span class="lead-line"></span><span class="time">9:00 - 10:00</span></div>
    <div class="row"><span class="day">Friday</span><span class="lead-line"></span><span class="time">9:00 - 10:00</span></div>
    <div class="row"><span class="day">Saturday</span><span class="lead-line"></span><span class="time">9:00 - 10:00</span></div>
    <div class="row"><span class="day">Sunday</span><span class="lead-line"></span><span class="time">Closed</span></div>
  </div>

  <div class="footer-rule"></div>
  <p class="copyright">©2022 Tidewell Bodyworks.All rights reserved.</p>
</div>
</body>
</html>
```